Commercial Swimming Pool - Design-Build Contractor Website Design

I need a new website that will feature our newly developed logo and trade name as well as provide a fully updated site experience. We are not a residential builder - we strictly design and install high-end commercial pools. I need the website to highlight our portfolio and communicate the various types of projects in which we specialize. I want the effect of the site to reflect the high-end nature of our services - projects like the 57th floor spa at the Delmar Brightwater, the aquatic therapy portion of the Delmar Falcons training facility, a 5om indoor competition pool for the prestigious Thornwick Academy, the indoor water park at The Calloway Lodge or the recent country club renovation projects we've completed in our region (to name a few examples).

```html
<!DOCTYPE html>
<html lang="en">
<head>
<meta charset="utf-8">
<title>Corwell Aquatics — Commercial Pool Design &amp; Build</title>
<link rel="stylesheet" href="https://fonts.googleapis.com/css2?family=Montserrat:wght@400;500;600;700;800&display=swap">
<style>
:root{
  --navy:#1b2a5c;
  --navy-deep:#14204a;
  --sky:#3ba7df;
  --sky-light:#bfe3f5;
  --pool:#2d8fd0;
  --pool-dark:#1f6fa8;
  --text:#3a3f4a;
  --muted:#8a909c;
  --card:#f3f4f6;
  --line:#c9ced8;
  --white:#ffffff;
}
*{box-sizing:border-box;margin:0;padding:0}
html,body{width:1200px;height:4758px;overflow:hidden}
body{position:relative;background:var(--white);font-family:"Montserrat",sans-serif;color:var(--text)}
.abs{position:absolute}
.btn{position:absolute;display:flex;align-items:center;justify-content:center;background:var(--navy);color:var(--white);font-size:16px;font-weight:500;border-radius:6px}

/* header */
.nav-link{position:absolute;top:52px;font-size:16px;font-weight:500;color:var(--navy)}
.nav-link.active{color:var(--sky)}
.brand{position:absolute;display:flex;align-items:center;gap:10px;font-weight:700;color:var(--navy);letter-spacing:1px}
.brand-dot{border-radius:50%;background:var(--sky)}
.social{position:absolute;width:26px;height:26px;border-radius:50%;background:var(--navy)}
.call{position:absolute;left:917px;top:41px;width:187px;height:51px;background:var(--navy);border-radius:6px;color:var(--white);text-align:center}
.call small{display:block;font-size:15px;margin-top:5px;padding-left:22px}
.call strong{display:block;font-size:18px;font-weight:700;padding-left:22px}
.call-icon{position:absolute;left:-10px;top:13px;width:26px;height:26px;border-radius:50%;background:var(--sky)}

/* hero */
.hero-photo{position:absolute;left:0;top:124px;width:1200px;height:570px;background:linear-gradient(160deg,#5aa7cf 0%,#2f7fb6 45%,#3a8cc3 70%,#1f5f96 100%)}
.hero-frame{position:absolute;left:151px;top:271px;width:670px;height:231px;border:1.5px solid rgba(255,255,255,.8)}
.hero-kicker{position:absolute;left:183px;top:305px;font-size:38px;font-weight:400;color:var(--white);letter-spacing:.5px}
.hero-title{position:absolute;left:181px;top:347px;font-size:58px;font-weight:800;color:var(--white);letter-spacing:-.5px}

/* about */
.about-back{position:absolute;left:114px;top:788px;width:475px;height:320px;border-radius:14px;background:linear-gradient(135deg,#7cc7ec,#3a96d6)}
.about-photo{position:absolute;left:153px;top:840px;width:447px;height:295px;border-radius:12px;background:linear-gradient(180deg,#6c8a5a 0%,#4f7a4a 40%,#49b4dc 62%,#2a9fd6 100%);box-shadow:0 10px 24px rgba(0,0,0,.25)}
.section-title{position:absolute;font-size:32px;font-weight:800;color:var(--navy)}
.about-text{position:absolute;left:646px;top:874px;width:447px;font-size:15.5px;line-height:25.8px;text-align:justify}

/* portfolio */
.tile{position:absolute}
.wave{position:absolute;left:0;width:1200px}

/* projects */
.project{position:absolute;left:89px;width:1026px;height:274px;background:var(--card)}
.project-tag{position:absolute;left:42px;top:137px;transform:translate(-50%,-50%) rotate(-90deg);white-space:nowrap;font-weight:800;color:var(--navy)}
.project-photo{position:absolute;left:73px;top:35px;width:359px;height:207px}
.project-body{position:absolute;left:467px;top:44px;width:520px}
.project-body h3{font-size:21px;font-weight:800;color:var(--navy);line-height:29px;letter-spacing:-.3px;text-transform:uppercase}
.project-body p{font-size:16px;line-height:29px;margin-top:8px}
.learn{display:block;margin-top:12px;font-size:16px;color:var(--sky)}

/* contact */
.contact-band{position:absolute;left:0;top:3744px;width:1200px;height:640px;background:linear-gradient(160deg,#47acdf,#2f95d3 50%,#3ea3dc)}
.contact-title{position:absolute;left:0;top:3790px;width:1200px;text-align:center;font-size:32px;font-weight:800;color:var(--white)}
.contact-intro{position:absolute;left:230px;top:3854px;width:740px;text-align:center;font-size:16px;line-height:26px;color:var(--white)}
.form-panel{position:absolute;left:271px;top:3934px;width:658px;height:347px;background:#fafafa;border-radius:4px}
.field{position:absolute;border:1px solid var(--line);border-radius:6px;font-size:11px;color:var(--muted);padding:12px 14px;background:var(--white)}

/* footer */
.foot-head{position:absolute;top:4462px;font-size:17px;font-weight:600;color:var(--navy)}
.foot-item{position:absolute;font-size:16px;line-height:26px;color:var(--text)}
.foot-link{position:absolute;left:672px;font-size:16px;color:var(--text)}
.rule{position:absolute;left:0;top:4683px;width:1200px;height:1px;background:#d6dae2}
.copyright{position:absolute;left:0;top:4702px;width:1200px;text-align:center;font-size:14px;color:var(--text)}
</style>
</head>
<body>

<!-- header -->
<a class="nav-link active" style="left:114px">Home</a>
<a class="nav-link" style="left:198px">About</a>
<a class="nav-link" style="left:284px">Portfolio</a>
<a class="nav-link" style="left:389px">Projects</a>
<div class="brand" style="left:505px;top:44px;font-size:22px">
  <span class="brand-dot" style="width:26px;height:26px"></span>Corwell Aquatics
</div>
<span class="social" style="left:755px;top:52px"></span>
<span class="social" style="left:794px;top:52px"></span>
<span class="social" style="left:833px;top:52px"></span>
<div class="call">
  <span class="call-icon"></span>
  <small>Call Us</small>
  <strong>(+1) 888 888 8888</strong>
</div>

<!-- hero -->
<div class="hero-photo" role="img" aria-label="Swimmers racing in lanes of a competition pool"></div>
<svg class="wave" style="top:600px" width="1200" height="100" viewBox="0 0 1200 100" preserveAspectRatio="none">
  <path d="M0 55 C250 95 500 95 750 70 C950 50 1100 40 1200 30 L1200 100 L0 100 Z" fill="#bfe3f5"/>
  <path d="M0 70 C250 105 500 100 750 80 C950 62 1100 55 1200 48 L1200 100 L0 100 Z" fill="#ffffff"/>
</svg>
<div class="hero-frame"></div>
<div class="hero-kicker">WELCOME TO</div>
<h1 class="hero-title">CORWELL AQUATICS</h1>
<a class="btn" style="left:183px;top:432px;width:151px;height:40px">Get Started</a>

<!-- about -->
<div class="about-back" role="img" aria-label="Rippling pool water"></div>
<div class="about-photo" role="img" aria-label="Resort pool with palm trees and ocean view"></div>
<h2 class="section-title" style="left:646px;top:815px">ABOUT US</h2>
<p class="about-text">Lorem ipsum dolor sit amet, consectetur adipiscing elit, sed do eiusmod tempor incididunt ut labore et dolore magna aliqua. Quis ipsum suspendisse ultrices gravida. Risus commodo viverra maecenas accumsan lacus vel facilisis. Lorem ipsum dolor sit amet, consectetur adipiscing elit, sed do eiusmod tempor incididunt ut labore et dolore magna aliqua.</p>
<a class="btn" style="left:644px;top:1080px;width:135px;height:40px">Read More</a>

<!-- portfolio -->
<h2 class="section-title" style="left:0;width:1200px;text-align:center;top:1257px">PORTFOLIO</h2>
<div class="tile" style="left:113px;top:1357px;width:618px;height:386px;background:linear-gradient(160deg,#8fd6ef,#2fb0e0 50%,#1a8ec9)" role="img" aria-label="Indoor competition pool with lane ropes"></div>
<div class="tile" style="left:753px;top:1357px;width:340px;height:221px;background:linear-gradient(180deg,#5d94c8 0%,#6f8c5c 45%,#2fb4d6 70%,#1c8fb8)" role="img" aria-label="Outdoor pool with palm trees"></div>
<div class="tile" style="left:753px;top:1604px;width:340px;height:445px;background:linear-gradient(180deg,#d7e4ee 0%,#a9c2d4 40%,#3fb3d8 70%,#2c6f8c)" role="img" aria-label="Indoor pool hall with glass roof"></div>
<div class="tile" style="left:113px;top:1765px;width:264px;height:284px;background:linear-gradient(160deg,#5e7a4c,#3d67b5 45%,#2f5fb0 70%,#6c6e6a)" role="img" aria-label="Aerial view of a mosaic-tiled pool"></div>
<div class="tile" style="left:393px;top:1765px;width:338px;height:284px;background:linear-gradient(180deg,#2e8fd3,#4cb7ec 50%,#1e6fb8)" role="img" aria-label="Underwater view of pool lanes"></div>
<a class="btn" style="left:533px;top:2095px;width:135px;height:43px">View More</a>
<svg class="wave" style="top:2180px" width="1200" height="60" viewBox="0 0 1200 60" preserveAspectRatio="none">
  <path d="M0 30 C200 10 400 45 650 35 C850 27 1050 10 1200 22 L1200 40 C1050 30 850 45 650 50 C400 60 200 30 0 45 Z" fill="#d9eef9"/>
</svg>

<!-- projects -->
<h2 class="section-title" style="left:0;width:1200px;text-align:center;top:2303px">PROJECTS</h2>

<article class="project" style="top:2404px">
  <span class="project-tag" style="font-size:25px">NEW PROJECT</span>
  <div class="project-photo" style="background:linear-gradient(180deg,#1a1f40,#3b3f86 45%,#7dd6c9 75%,#2a5a7a)" role="img" aria-label="Rooftop spa pool lit at night"></div>
  <div class="project-body">
    <h3>57th floor spa at the Delmar Brightwater seasons</h3>
    <p>Lorem ipsum dolor sit amet, consectetur adipiscing elit, sed do eiusmod tempor incididunt ut labore et dolore magna aliqua. Quis ipsum suspendisse ultrices gravida.</p>
    <a class="learn">Learn More ›</a>
  </div>
</article>

<article class="project" style="top:2701px">
  <span class="project-tag" style="font-size:20px">UPCOMING PROJECT</span>
  <div class="project-photo" style="background:linear-gradient(135deg,#4c6a3e,#3d66b3 50%,#c9cbc8)" role="img" aria-label="Tiled pool beside a hotel balcony"></div>
  <div class="project-body">
    <h3>The aquatic therapy portion of the Delmar Falcons training facility,</h3>
    <p>Lorem ipsum dolor sit amet, consectetur adipiscing elit, sed do eiusmod tempor incididunt ut labore et dolore magna aliqua. Quis ipsum suspendisse ultrices gravida.</p>
    <a class="learn">Learn More ›</a>
  </div>
</article>

<article class="project" style="top:2996px">
  <span class="project-tag" style="font-size:20px">UPCOMING PROJECT</span>
  <div class="project-photo" style="background:linear-gradient(180deg,#2a2a66,#3a3fa8 45%,#3aa0e8 70%,#1f5fb0)" role="img" aria-label="Illuminated pool with palm trees at night"></div>
  <div class="project-body">
    <h3>A 50m indoor competition pool for the prestigious Thornwick Academy,</h3>
    <p>Lorem ipsum dolor sit amet, consectetur adipiscing elit, sed do eiusmod tempor incididunt ut labore et dolore magna aliqua. Quis ipsum suspendisse ultrices gravida.</p>
    <a class="learn">Learn More ›</a>
  </div>
</article>

<article class="project" style="top:3291px">
  <span class="project-tag" style="font-size:25px">NEW PROJECT</span>
  <div class="project-photo" style="background:linear-gradient(180deg,#6c8a5a 0%,#4f7a4a 40%,#49b4dc 62%,#2a9fd6 100%)" role="img" aria-label="Resort pool with palm trees and sea view"></div>
  <div class="project-body">
    <h3>The indoor water park at The Calloway Lodge or the recent country club renovation projects</h3>
    <p>Lorem ipsum dolor sit amet, consectetur adipiscing elit, sed do eiusmod tempor incididunt ut labore et dolore magna aliqua.</p>
    <a class="learn">Learn More ›</a>
  </div>
</article>

<a class="btn" style="left:533px;top:3622px;width:135px;height:42px">View More</a>

<!-- contact -->
<div class="contact-band" role="img" aria-label="Sunlit pool water surface"></div>
<svg class="wave" style="top:4335px" width="1200" height="60" viewBox="0 0 1200 60" preserveAspectRatio="none">
  <path d="M0 20 C300 50 600 40 900 25 C1050 18 1130 15 1200 18 L1200 60 L0 60 Z" fill="#bfe3f5"/>
  <path d="M0 32 C300 60 600 52 900 38 C1050 30 1130 28 1200 30 L1200 60 L0 60 Z" fill="#ffffff"/>
</svg>
<h2 class="contact-title">GET IN TOUCH!</h2>
<p class="contact-intro">Lorem ipsum dolor sit amet, consectetur adipiscing elit, sed do eiusmod tempor incididunt ut labore et dolore magna aliqua. Quis ipsum suspendisse ultrices gravida.</p>
<form class="form-panel">
  <div class="field" style="left:41px;top:50px;width:268px;height:40px">First Name</div>
  <div class="field" style="left:340px;top:50px;width:266px;height:40px">Last Name</div>
  <div class="field" style="left:41px;top:107px;width:268px;height:40px">Phone Number</div>
  <div class="field" style="left:340px;top:107px;width:268px;height:40px">Email</div>
  <div class="field" style="left:41px;top:164px;width:567px;height:76px">Your Message</div>
  <a class="btn" style="left:259px;top:271px;width:142px;height:41px">Submit</a>
</form>

<!-- footer -->
<div class="brand" style="left:107px;top:4480px;font-size:20px">
  <span class="brand-dot" style="width:24px;height:24px"></span>Corwell Aquatics
</div>
<span class="social" style="left:127px;top:4556px"></span>
<span class="social" style="left:172px;top:4556px"></span>
<span class="social" style="left:216px;top:4556px"></span>

<h4 class="foot-head" style="left:404px">Contact</h4>
<svg class="abs" style="left:404px;top:4510px" width="12" height="16" viewBox="0 0 12 16"><path d="M6 0a6 6 0 0 0-6 6c0 4.5 6 10 6 10s6-5.5 6-10a6 6 0 0 0-6-6zm0 8.3a2.3 2.3 0 1 1 0-4.6 2.3 2.3 0 0 1 0 4.6z" fill="#1b2a5c"/></svg>
<p class="foot-item" style="left:430px;top:4503px;width:150px">#1, Sample Street, Sample City, USA 72364.</p>
<svg class="abs" style="left:404px;top:4591px" width="12" height="12" viewBox="0 0 24 24"><path d="M6.6 10.8a15 15 0 0 0 6.6 6.6l2.2-2.2a1 1 0 0 1 1-.25 11.4 11.4 0 0 0 3.6.6 1 1 0 0 1 1 1V20a1 1 0 0 1-1 1A17 17 0 0 1 3 4a1 1 0 0 1 1-1h3.5a1 1 0 0 1 1 1c0 1.25.2 2.45.6 3.6a1 1 0 0 1-.25 1z" fill="#1b2a5c"/></svg>
<p class="foot-item" style="left:430px;top:4584px">+1 (888) 888 8888</p>
<svg class="abs" style="left:404px;top:4629px" width="12" height="9" viewBox="0 0 12 9"><rect width="12" height="9" rx="1" fill="#1b2a5c"/><path d="M0.5 1 6 5 11.5 1" stroke="#fff" fill="none"/></svg>
<p class="foot-item" style="left:430px;top:4621px">info@corwellaquatics.com</p>

<h4 class="foot-head" style="left:672px">Quick Links</h4>
<a class="foot-link" style="top:4504px">Home</a>
<a class="foot-link" style="top:4533px">About</a>
<a class="foot-link" style="top:4562px">Portfolio</a>
<a class="foot-link" style="top:4591px">Project</a>
<a class="foot-link" style="top:4620px">Contact</a>

<h4 class="foot-head" style="left:834px">Subscribe</h4>
<div class="field" style="left:834px;top:4502px;width:262px;height:43px;font-size:14px">Email</div>
<a class="btn" style="left:834px;top:4563px;width:120px;height:37px;font-size:14px">Submit</a>

<div class="rule"></div>
<p class="copyright">© copyrights 2023 Corwell Aquatics | All Rights Reserved</p>

</body>
</html>
```